Professional Website Design to match new logo for Medical Legal Company

We have rebranded our company and We want a professional but also dynamic web site design for a group of esteemed doctors that provide expert evaluation of an injured worker in a Workers Compensation case.
​
1. Our target market is both the attorneys who select our doctors and any doctors who would wish to join our group.

2. Notes for the Landing Page:
- We prefer a simpler, sleeker more modern look for the landing page.
- We want a simplified landing page with one image, three buttons highlighted in Content document.
- We want the main image to be black and white but it can be splashed with color.
-We think the landing page might be enhanced by add a dark blue or black as a primary color. Of course please feel free to try any color combination you think might work.
- We want "The Meridale Circle" in large letters and "Stewards of a fair and prompt outcome" in small lettering. We don't want icons on the buttons.
- Do not want more than the one picture at top of landing page.
- We do not want any pictures that include faces. Please eliminate or replace. They will not be chosen.
- For the landing page, instead of a second set of photos please experiment with using medical symbols and legal symbols.
​
3. New Company Name: The Meridale Circle
New logo is uploaded bronze and grey/silver will be colors although we are still tweaking the colors for more metallic feel. Want simple not busy.

4. The overall Web page design needs to have some website design effect (e,g image rollover, scrolling effect, hover effect etc).

5. Please follow the attached word document file for the page content of the 4 web pages. Do not mix it up.

Previous company website: www.clinicjuristpanel.example (we wish to convert some of the content from this website to the new brand). Competitor website that we like: www.docboardly.example

Target Market(s)

Professional Elite. Attorneys and Doctors

Industry/Entity Type

Medical Legal

Coding

Coded - Design and coding required

Number of Pages Required

5+ page

Font styles to use
Other font styles liked:
• Helvetica or maybe font that matches logo. We are open

Colors

Designer to choose colors to be used in the design.

Requirements
Must have
• I can't locate on color scale but we want Bronze and Silver/Grey from logo. Additional colors can be added. Various shades of grey
Nice to have
• Black and white photos, simple elegant design
Should not have
• Images with faces of unknown people

```html
<!DOCTYPE html>
<html lang="en">
<head>
<meta charset="utf-8">
<title>The Meridale Circle</title>
<link rel="stylesheet" href="https://fonts.googleapis.com/css2?family=Inter:wght@300;400;500;600&family=Playfair+Display:wght@400;600;700&display=swap">
<style>
  :root {
    --bronze: #b97a52;
    --bronze-soft: #c9875c;
    --bronze-deep: #3a1d0c;
    --banner: #9a6f56;
    --ink: #111111;
    --text: #2a2a2a;
    --nav: #2e2e30;
    --card-top: #3a393d;
    --card-bottom: #1e1d21;
    --footer: #1c1c1e;
    --footer-text: #e6e6e6;
    --white: #ffffff;
  }
  * { box-sizing: border-box; margin: 0; padding: 0; }
  html, body { width: 999px; height: 1200px; overflow: hidden; background: var(--white); }
  body { position: relative; font-family: "Inter", Helvetica, Arial, sans-serif; color: var(--text); }

  .site-header {
    position: absolute; left: 0; top: 0; width: 999px; height: 83px;
    background: linear-gradient(90deg, #d2d2d2 0%, #c4c4c4 45%, #dcdcdc 100%);
    border-bottom: 3px solid var(--bronze);
  }
  .brand {
    position: absolute; display: flex; align-items: center; gap: 8px;
    font-family: "Playfair Display", Georgia, serif; font-weight: 600; letter-spacing: 0.5px;
  }
  .brand-dot { width: 14px; height: 14px; border-radius: 50%; background: var(--bronze); }
  .site-header .brand { left: 92px; top: 26px; font-size: 24px; color: #5a5a5c; }
  .main-nav { position: absolute; top: 38px; left: 532px; display: flex; font-size: 14px; font-weight: 500; color: var(--nav); }
  .main-nav a { color: inherit; text-decoration: none; position: absolute; white-space: nowrap; }

  .hero { position: absolute; left: 0; top: 83px; width: 999px; height: 430px; }
  .hero svg { display: block; }
  .hero-title {
    position: absolute; left: 0; width: 999px; top: 218px; text-align: center;
    font-family: "Playfair Display", Georgia, serif; font-weight: 600; font-size: 54px;
    color: var(--white); letter-spacing: -0.5px; line-height: 1;
  }
  .hero-tagline {
    position: absolute; left: 0; width: 999px; top: 287px; text-align: center;
    font-weight: 300; font-size: 17px; color: var(--white);
  }

  .audience-card {
    position: absolute; top: 424px; width: 265px; height: 131px; border-radius: 12px;
    border: 2px solid var(--bronze);
    background: linear-gradient(180deg, var(--card-top), var(--card-bottom));
    box-shadow: 0 22px 40px rgba(229, 150, 110, 0.22);
    text-align: center; color: var(--white);
  }
  .audience-card.featured { background: linear-gradient(180deg, #b87a52 0%, #7a4a2c 55%, var(--bronze-deep) 100%); top: 422px; }
  .card-title { font-family: "Playfair Display", Georgia, serif; font-size: 23px; line-height: 30px; font-weight: 400; }
  .card-sub { font-size: 11px; margin-top: 6px; }
  .card-button {
    position: absolute; left: 50%; transform: translateX(-50%); width: 94px; height: 20px; border-radius: 10px;
    background: var(--bronze); color: var(--white); font-size: 10px; font-weight: 500; line-height: 20px;
  }

  .intro {
    position: absolute; left: 150px; width: 700px; top: 638px; text-align: center;
    font-size: 16.5px; font-weight: 300; line-height: 20px; color: var(--ink);
  }
  .intro strong { font-weight: 500; }

  .newsletter {
    position: absolute; left: 90px; top: 766px; width: 819px; height: 140px; border-radius: 16px;
    background: linear-gradient(90deg, #9b7059 0%, #98684f 60%, #a17058 100%);
  }
  .newsletter-title { position: absolute; left: 51px; top: 54px; font-size: 25px; font-weight: 500; color: var(--white); }
  .download-button {
    position: absolute; left: 604px; top: 60px; width: 172px; height: 37px; border-radius: 8px;
    background: #000; color: var(--white); font-size: 14px; font-weight: 600;
    display: flex; align-items: center; justify-content: center; gap: 14px;
  }

  .site-footer { position: absolute; left: 0; top: 986px; width: 999px; height: 214px; background: var(--footer); }
  .footer-rule { position: absolute; left: 80px; top: 0; width: 919px; height: 2px; background: var(--bronze); }
  .site-footer .brand { left: 71px; top: 40px; font-size: 20px; color: #8a8a8e; }
  .footer-divider { position: absolute; width: 1px; background: var(--bronze); }
  .footer-heading {
    position: absolute; font-family: "Playfair Display", Georgia, serif; font-size: 14px;
    color: var(--bronze-soft); letter-spacing: 0.3px; white-space: nowrap;
  }
  .footer-text { position: absolute; font-size: 11px; line-height: 13px; color: var(--footer-text); }
  .footer-links a {
    position: absolute; font-size: 11px; font-weight: 600; color: var(--footer-text); text-decoration: none; white-space: nowrap;
  }
  .social-dot { position: absolute; width: 16px; height: 16px; border-radius: 50%; background: var(--bronze); }
  .copyright { position: absolute; left: 71px; top: 160px; font-family: "Playfair Display", Georgia, serif; font-size: 8px; color: var(--footer-text); }
</style>
</head>
<body>

<header class="site-header">
  <div class="brand"><span class="brand-dot"></span>Meridale Circle</div>
  <nav class="main-nav">
    <a href="#" style="left:0">PHYSICIANS</a>
    <a href="#" style="left:137px">STAKEHOLDER</a>
    <a href="#" style="left:273px">CIRCLE GIVES</a>
  </nav>
</header>

<section class="hero">
  <svg width="999" height="430" viewBox="0 0 999 430" role="img" aria-label="Black and white photograph of a judge's gavel resting beside a stethoscope">
    <defs>
      <linearGradient id="heroTone" x1="0" y1="0" x2="1" y2="0.4">
        <stop offset="0" stop-color="#050505"/>
        <stop offset="0.45" stop-color="#1a1a1a"/>
        <stop offset="0.8" stop-color="#4a4a4a"/>
        <stop offset="1" stop-color="#6a6a6a"/>
      </linearGradient>
    </defs>
    <path d="M0 0 H999 V391 Q500 440 0 391 Z" fill="url(#heroTone)"/>
  </svg>
  <h1 class="hero-title">THE MERIDALE CIRCLE</h1>
  <p class="hero-tagline">Stewards of a fair and prompt outcome</p>
</section>

<article class="audience-card" style="left:95px">
  <h2 class="card-title" style="margin-top:32px">STAKEHOLDERS</h2>
  <p class="card-sub">Attorneys, Carriers, Injured Workers</p>
  <span class="card-button" style="top:91px;left:121px">LEARN MORE</span>
</article>
<article class="audience-card featured" style="left:374px">
  <h2 class="card-title" style="margin-top:34px">QME PHYSICIANS</h2>
  <span class="card-button" style="top:88px">LEARN MORE</span>
</article>
<article class="audience-card" style="left:654px">
  <h2 class="card-title" style="margin-top:24px">MEMBER<br>PHYSICIANS</h2>
  <span class="card-button" style="top:91px">LEARN MORE</span>
</article>

<p class="intro"><strong>The Meridale Circle</strong> is a leader in Qualified Medical Evaluations and SIBTF cases in the State of California. Our doctors are dedicated to facilitating settlements through rapid, objective and well researched Expert Medical Opinions</p>

<section class="newsletter">
  <h3 class="newsletter-title">Most Recent Newsletter</h3>
  <a class="download-button">DOWNLOAD
    <svg width="18" height="16" viewBox="0 0 18 16" fill="none" stroke="#fff" stroke-width="1.6" stroke-linecap="round" stroke-linejoin="round">
      <path d="M9 1 V10 M5 6.5 L9 10.5 L13 6.5 M1.5 11 V14.5 H16.5 V11"/>
    </svg>
  </a>
</section>

<footer class="site-footer">
  <div class="footer-rule"></div>
  <div class="brand"><span class="brand-dot"></span>Meridale Circle</div>
  <p class="copyright">© 2024 Clinic Jurist Panel</p>

  <div class="footer-divider" style="left:276px;top:36px;height:130px"></div>
  <div class="footer-divider" style="left:528px;top:41px;height:130px"></div>
  <div class="footer-divider" style="left:527px;top:89px;height:33px;width:3px"></div>
  <div class="footer-divider" style="left:735px;top:32px;height:130px"></div>

  <h4 class="footer-heading" style="left:326px;top:35px">COMPANY INFO</h4>
  <p class="footer-text" style="left:330px;top:72px">HEADQUARTERS<br>2750 Larkspur Ave.<br>4th Floor<br>Brenton, CA 90000</p>
  <p class="footer-text" style="left:330px;top:147px">Call toll free (800) 555-0142<br>Fax (310) 555-0187</p>

  <h4 class="footer-heading" style="left:570px;top:40px">QUICKLINKS</h4>
  <nav class="footer-links">
    <a href="#" style="left:575px;top:75px">PHYSICIANS</a>
    <a href="#" style="left:575px;top:101px">STAKEHOLDER</a>
    <a href="#" style="left:575px;top:128px">CIRCLE GIVES</a>
  </nav>

  <h4 class="footer-heading" style="left:781px;top:37px">CONNECT WITH US</h4>
  <span class="social-dot" style="left:783px;top:68px"></span>
  <span class="social-dot" style="left:810px;top:68px"></span>
  <span class="social-dot" style="left:842px;top:68px"></span>
</footer>

</body>
</html>
```